Heavy Duty Repairs Poster

Good afternoon - I'm looking for a poster , design to set up around different areas. The Poster must consist of the following
- Heavy duty repairs
- Pictures of Semi trucks , heavy construction equipment , trailers
- Agriculture
- All north American equipment ( see attached pictures)
- Brief Descriptions in bullet point forms
CVIPS
WELDING
AIR CONDITIONING
ENGINE REBUILDS
DIAGONSTICS
FLEET MANAGMENT
TIRE REPAIR AND SALES
ELECTRICAL , HYDRALIC , POWER TRAIN SERVICE AND REPAIRS
PART SALES
FLEET MAINTINACE
DELTEING AND TUNING
AFTER MARKET INSTALLS OUTFITTING
ONSITE & OFFSITE REPAIRS
FULL RECERTIFACTION OVERHAULING
Warranty Approved

Target Market(s)

Heavy Duty Truck , Equipment , Agriculture Owners

Industry/Entity Type

Heavy Duty Repairs

Colors
EB3D1F
EC4F4E
F09395
F8D3D4
FCEDEE

Requirements
Must have
• Pictures of : Semi trucks and trailer , Construction heavy equipment , agriculture equipment
Nice to have
• Flashy and stands out

```html
<!DOCTYPE html>
<html lang="en">
<head>
<meta charset="utf-8">
<title>Heavy Duty Repairs Poster</title>
<link rel="stylesheet" href="https://fonts.googleapis.com/css2?family=Archivo+Black&family=Bebas+Neue&family=Montserrat:wght@400;600&display=swap">
<style>
  :root {
    --page: #ffffff;
    --red: #f81116;
    --red-photo-top: #f7676a;
    --red-photo-mid: #ee3b3f;
    --truck-red: #b81a22;
    --truck-grey: #c9c2c0;
    --truck-dark: #4a3a3a;
    --white: #ffffff;
    --ink: #000000;
    --footer: #000000;
    --phone-red: #e0141a;
    --gold: #d6a93a;
    --gold-dark: #8a6418;
    --badge-core: #1d1d1d;
  }
  * { margin: 0; padding: 0; box-sizing: border-box; }
  html, body {
    width: 1200px; height: 1200px; overflow: hidden;
    background: var(--page);
  }
  .poster {
    position: absolute; left: 165px; top: 37px;
    width: 870px; height: 1124px;
    background: var(--red); overflow: hidden;
  }
  .hero-photo {
    position: absolute; left: 0; top: 0; width: 870px; height: 700px;
    background: linear-gradient(180deg, var(--red-photo-top) 0%, var(--red-photo-mid) 55%, var(--red) 100%);
  }
  .truck-photo {
    position: absolute; left: 531px; top: 174px; width: 310px; height: 342px;
    border-radius: 6px;
    background: linear-gradient(180deg, var(--truck-grey) 0%, var(--truck-grey) 24%, var(--truck-red) 34%, var(--truck-red) 58%, var(--truck-grey) 72%, var(--truck-dark) 100%);
  }
  .headline-group { font-weight: normal; }
  .headline {
    position: absolute; font-family: "Bebas Neue", sans-serif;
    color: var(--white); line-height: 1; white-space: nowrap;
  }
  .headline--h { left: 85px; top: 6px; font-size: 275px; transform: scaleX(0.82); transform-origin: left top; }
  .headline--eavy { left: 190px; top: 33px; font-size: 243px; letter-spacing: 1px; }
  .headline--duty { left: 85px; top: 235px; font-size: 243px; }
  .headline--repairs { left: 85px; top: 435px; font-size: 243px; letter-spacing: 3px; }

  .services {
    position: absolute; list-style: none;
    font-family: "Montserrat", sans-serif; font-weight: 400;
    font-size: 19.5px; line-height: 27.5px; color: var(--white);
  }
  .services--left { left: 77px; top: 676px; width: 380px; }
  .services--right { left: 435px; top: 676px; width: 430px; }
  .services li { position: relative; padding-left: 30px; white-space: nowrap; }
  .services .tick {
    position: absolute; left: 0; top: 3px; width: 23px; height: 21px;
  }

  .warranty-badge { position: absolute; left: 624px; top: 849px; width: 160px; height: 160px; }

  .footer {
    position: absolute; left: 0; top: 1003px; width: 870px; height: 121px;
    background: var(--footer);
  }
  .brand {
    position: absolute; left: 40px; top: 60px; width: 300px; text-align: center;
    font-family: "Montserrat", sans-serif; font-weight: 600; color: var(--white);
  }
  .brand__name { font-size: 19px; }
  .brand__place { font-size: 14px; margin-top: 3px; }
  .phone {
    position: absolute; left: 390px; top: 24px;
    font-family: "Archivo Black", sans-serif;
    font-size: 56px; line-height: 1; letter-spacing: 0;
    color: var(--phone-red);
  }
</style>
</head>
<body>
<main class="poster">
  <div class="hero-photo" role="img" aria-label="Red-tinted photo of a desert highway with snowy mountains behind"></div>
  <div class="truck-photo" role="img" aria-label="Photo of a red semi truck pulling a white box trailer toward the viewer"></div>

  <h1 class="headline-group">
    <span class="headline headline--h">H</span>
    <span class="headline headline--eavy">EAVY</span>
    <span class="headline headline--duty">DUTY</span>
    <span class="headline headline--repairs">REPAIRS</span>
  </h1>

  <svg width="0" height="0" style="position:absolute">
    <defs>
      <symbol id="tick" viewBox="0 0 23 21">
        <path d="M1 11 L4 8.5 L8.5 14 L20 1 L22 2.5 L9 20 Z" fill="#000"/>
      </symbol>
    </defs>
  </svg>

  <ul class="services services--left">
    <li><svg class="tick"><use href="#tick"/></svg>CVIPS</li>
    <li><svg class="tick"><use href="#tick"/></svg>WELDING</li>
    <li><svg class="tick"><use href="#tick"/></svg>AIR CONDITIONING</li>
    <li><svg class="tick"><use href="#tick"/></svg>ENGINE REBUILDS</li>
    <li><svg class="tick"><use href="#tick"/></svg>DIAGONSTICS</li>
    <li><svg class="tick"><use href="#tick"/></svg>FLEET MANAGMENT</li>
    <li><svg class="tick"><use href="#tick"/></svg>TIRE REPAIR AND SALES</li>
    <li><svg class="tick"><use href="#tick"/></svg>ELECTRICAL , HYDRALIC , POWER<br>TRAIN SERVICE AND REPAIRS</li>
  </ul>

  <ul class="services services--right">
    <li><svg class="tick"><use href="#tick"/></svg>PART SALES</li>
    <li><svg class="tick"><use href="#tick"/></svg>FLEET MAINTINACE</li>
    <li><svg class="tick"><use href="#tick"/></svg>DELTEING AND TUNING</li>
    <li><svg class="tick"><use href="#tick"/></svg>AFTER MARKET INSTALLS OUTFITTING</li>
    <li><svg class="tick"><use href="#tick"/></svg>ONSITE &amp; OFFSITE REPAIRS</li>
    <li><svg class="tick"><use href="#tick"/></svg>FULL RECERTIFACTION OVERHAULING</li>
  </ul>

  <svg class="warranty-badge" viewBox="0 0 160 160" aria-hidden="true">
    <circle cx="80" cy="80" r="79" fill="var(--gold-dark)"/>
    <circle cx="80" cy="80" r="75" fill="var(--gold)"/>
    <circle cx="80" cy="80" r="50" fill="var(--badge-core)"/>
  </svg>

  <footer class="footer">
    <div class="brand">
      <div class="brand__name">Northgate Fleet Works</div>
      <div class="brand__place">Ridgemoor , Alberta</div>
    </div>
    <div class="phone">780-555-0147</div>
  </footer>
</main>
</body>
</html>
```